Thriving Mexican import business needs a new business card

Need a refresher of our current business card. Looking for a lighter background with the logo on one side. We will want this file to be adjustable so we can change names, emails and mobile numbers.
We are open to ideas but maintaining a professional image is critical.
Thankyou,

Target Market(s)

Anyone in food industry

Industry/Entity Type

Wholesale

Contact Information for Business Card

Mark Pendlebury
Director
Condor Provisions & Spirits Pty Ltd
5B Morrow Ct, Kelvinbrook VIC 3127
0421930576 (03) 95128460
mark@condorlatino.example.au
condorlatinoprovisionsandspirits.example.au

Font styles to use
Serif
Other font styles liked:
• NeoGram Heavy

Requirements
Must have
• Professional yet memorable
Condor logo
Nice to have
• Chilli or tequila/mexican food pictures
Should not have
• Dark background

```html
<!DOCTYPE html>
<html lang="en">
<head>
<meta charset="utf-8">
<title>Condor Provisions &amp; Spirits – Business Card</title>
<link href="https://fonts.googleapis.com/css2?family=Bebas+Neue&family=Open+Sans:wght@400&display=swap" rel="stylesheet">
<style>
  :root {
    --backdrop: #1c1c1c;
    --card: #ffffff;
    --ink: #0d0d0d;
  }
  * { box-sizing: border-box; margin: 0; padding: 0; }
  html, body {
    width: 1093px; height: 1200px; overflow: hidden;
    background: var(--backdrop);
  }
  .canvas { position: relative; width: 1093px; height: 1200px; }
  .card {
    position: absolute; left: 264px; width: 580px; height: 357px;
    background: var(--card); color: var(--ink);
    text-align: center;
  }
  .card--details { top: 226px; }
  .card--brand { top: 620px; width: 583px; }

  .name {
    position: absolute; left: 0; right: 0; top: 64px;
    font: 400 23px/1 "Bebas Neue", sans-serif; letter-spacing: 0.3px;
  }
  .role {
    position: absolute; left: 0; right: 0; top: 93px;
    font: 400 13.5px/1 "Open Sans", sans-serif; letter-spacing: 0.4px;
  }
  .rule {
    position: absolute; left: 213px; width: 154px; top: 116px;
    height: 1px; background: var(--ink);
  }
  .address {
    position: absolute; left: 0; right: 0; top: 130px;
    font: 400 14px/21px "Open Sans", sans-serif;
  }
  .icon-row {
    position: absolute; left: 213px; width: 154px; top: 186px; height: 24px;
    display: flex; align-items: center; justify-content: center; gap: 4px;
  }
  .icon-row .dash { flex: 1; height: 1px; background: var(--ink); }
  .icon-row .dash:first-child { margin-right: 3px; }
  .icon-row .dash:last-child { margin-left: 3px; }
  .icon {
    width: 24px; height: 24px; border-radius: 3px; background: var(--ink);
    display: flex; align-items: center; justify-content: center;
  }
  .contact {
    position: absolute; left: 0; right: 0; top: 220px;
    font: 400 13.5px/21px "Open Sans", sans-serif;
  }

  .brand-mark {
    position: absolute; left: 50%; top: 94px;
    width: 64px; height: 64px; margin-left: -32px;
    background: var(--ink);
  }
  .brand-name {
    position: absolute; left: 0; right: 0; top: 184px;
    font: 400 30px/40px "Open Sans", sans-serif; letter-spacing: 1px;
  }
</style>
</head>
<body>
<main class="canvas">
  <section class="card card--details">
    <h1 class="name">Mark Pendlebury</h1>
    <p class="role">DIRECTOR</p>
    <div class="rule"></div>
    <p class="address">5B Morrow Ct<br>Kelvinbrook VIC 3127</p>
    <div class="icon-row">
      <span class="dash"></span>
      <span class="icon" aria-label="Phone">
        <svg width="16" height="14" viewBox="0 0 16 14" fill="none" stroke="#fff" stroke-width="1.2">
          <path d="M1 5c0-2 3-3 7-3s7 1 7 3v1h-3V4.5H4V6H1z" fill="#fff"/>
          <rect x="3" y="7" width="10" height="6" rx="1"/>
          <circle cx="8" cy="10" r="1.3"/>
        </svg>
      </span>
      <span class="icon" aria-label="Email">
        <svg width="16" height="12" viewBox="0 0 16 12" fill="none" stroke="#fff" stroke-width="1.2">
          <rect x="0.8" y="0.8" width="14.4" height="10.4"/>
          <path d="M1 1l7 6 7-6M1 11l5-5M15 11l-5-5"/>
        </svg>
      </span>
      <span class="icon" aria-label="Website">
        <svg width="16" height="16" viewBox="0 0 16 16">
          <circle cx="8" cy="8" r="7" fill="#fff"/>
          <path d="M5 3c2 0 3 1 2 3s-3 1-3 3 2 2 1 4M10 4c1 1 3 2 2 4s-2 1-2 3" fill="none" stroke="#0d0d0d" stroke-width="1.4"/>
        </svg>
      </span>
      <span class="dash"></span>
    </div>
    <p class="contact">
      0421930576 (03) 95128460<br>
      mark@condorlatino.example.au<br>
      condorlatinoprovisionsandspirits.example.au
    </p>
  </section>

  <section class="card card--brand">
    <div class="brand-mark" role="img" aria-label="Company emblem"></div>
    <p class="brand-name">CONDOR<br>PROVISIONS &amp; SPIRITS</p>
  </section>
</main>
</body>
</html>
```